bottle label/ product label for smoothies (ultra fresh)

Please create a bottle label for our smoothies for retail distribution.
It's important that the following key features are clearly stated:

Ultra-fresh

Handmade

No preservatives

Not heat-treated

No added sugar

The base of the product label should be transparent, so that the color and content of the smoothie can be seen clearly.

We are a young, dynamic company. Our values are honesty, ultra-freshness, and authenticity — and we are the only ones producing this type of product in our country. We are positioned in the premium segment.

Design style: Modern, clean, and natural — but not playful or childish.

Example product: Selu Vane (Mango, Pineapple, Lemon, Passion Fruit, Orange)

Wenn du möchtest, kann ich auch gleich einen konkreten Vorschlag für das Etikettendesign auf Englisch oder einen Entwurfstext für das Label selbst erstellen. Sag einfach Bescheid!

Target Market(s)

trade - convenience

Industry/Entity Type

trade

Font styles to use
Sans Serif

Requirements
Must have
• sales- features: Ultra-fresh Handmade No preservatives Not heat-treated No added sugar

```html
<!DOCTYPE html>
<html lang="en">
<head>
<meta charset="utf-8">
<title>verano – Selu Vane smoothie label</title>
<link rel="stylesheet" href="https://fonts.googleapis.com/css2?family=Poppins:wght@400;500;600&display=swap">
<style>
  :root {
    --ink: #1c1a17;
    --sun-core: #edb72b;
    --sun-edge: #d8921f;
    --cream: #f8ecc9;
    --juice: #f1c032;
    --juice-deep: #e8a92a;
    --slice: rgba(255, 240, 190, 0.35);
    --slice-line: rgba(255, 250, 230, 0.9);
  }
  * { margin: 0; padding: 0; box-sizing: border-box; }
  html, body { width: 1200px; height: 1111px; overflow: hidden; }
  body { font-family: "Poppins", sans-serif; color: var(--ink); position: relative; background: var(--cream); }

  .label-panel {
    position: absolute; left: 0; top: 0; width: 714px; height: 1111px;
    background: radial-gradient(circle at 50% 45%, var(--sun-core) 0%, #e6aa26 45%, var(--sun-edge) 100%);
  }
  .shelf-panel {
    position: absolute; left: 714px; top: 0; width: 486px; height: 1111px;
    background: var(--cream);
  }

  .abs { position: absolute; white-space: nowrap; line-height: 1; }

  .brand { font-weight: 600; letter-spacing: 0.5px; }
  .name { font-weight: 500; letter-spacing: -2px; }
  .claims { font-weight: 400; text-align: center; }
  .flavour { font-weight: 600; letter-spacing: -0.3px; }

  .slice { position: absolute; border-radius: 50%; background: var(--slice); border: 2px solid var(--slice-line); }

  /* main label */
  .label-panel .brand { left: 216px; top: 310px; font-size: 56px; }
  .label-panel .name-top { left: 146px; top: 375px; font-size: 150px; transform: rotate(6deg); transform-origin: left top; }
  .label-panel .name-bottom { left: 212px; top: 488px; font-size: 156px; }
  .label-panel .slice-large { left: 441px; top: 383px; width: 184px; height: 184px; }
  .label-panel .slice-small { left: 143px; top: 568px; width: 72px; height: 72px; }
  .label-panel .claims { left: 0; width: 656px; top: 657px; font-size: 21.5px; line-height: 37px; }
  .label-panel .flavour { left: 0; width: 656px; text-align: center; top: 772px; font-size: 27px; }

  /* label as applied, flat */
  .label-card {
    position: absolute; left: 811px; top: 420px; width: 292px; height: 440px;
    background: linear-gradient(180deg, var(--juice) 0%, var(--juice-deep) 100%);
    border-radius: 6px;
  }
  .label-card .brand { left: 68px; top: 38px; font-size: 34px; }
  .label-card .name-top { left: 48px; top: 112px; font-size: 80px; transform: rotate(5deg); transform-origin: left top; }
  .label-card .name-bottom { left: 78px; top: 180px; font-size: 84px; }
  .label-card .slice-large { left: 205px; top: 120px; width: 86px; height: 86px; }
  .label-card .slice-small { left: 52px; top: 235px; width: 30px; height: 30px; }
  .label-card .claims { left: 0; width: 292px; top: 312px; font-size: 12.5px; line-height: 23px; opacity: 0.85; }
  .label-card .flavour { left: 0; width: 292px; text-align: center; top: 394px; font-size: 16px; }

  .sep { margin: 0 0.5em; }
</style>
</head>
<body>
  <section class="label-panel">
    <div class="slice slice-large" role="img" aria-label="Line drawing of an orange slice"></div>
    <div class="slice slice-small" role="img" aria-label="Small line drawing of an orange slice"></div>
    <div class="abs brand">verano</div>
    <div class="abs name name-top">selu</div>
    <div class="abs name name-bottom">vane</div>
    <div class="abs claims">
      Ultra Fresh<span class="sep">|</span>Handmade<span class="sep">|</span>No Preservatives<br>
      Not Heat-Treated<span class="sep">|</span>No Added Sugar
    </div>
    <div class="abs flavour">Orange Flavour</div>
  </section>

  <section class="shelf-panel"></section>

  <section class="label-card">
    <div class="slice slice-large" role="img" aria-label="Line drawing of an orange slice"></div>
    <div class="slice slice-small" role="img" aria-label="Small line drawing of an orange slice"></div>
    <div class="abs brand">verano</div>
    <div class="abs name name-top">selu</div>
    <div class="abs name name-bottom">vane</div>
    <div class="abs claims">
      Ultra Fresh<span class="sep">|</span>Handmade<span class="sep">|</span>No Preservatives<br>
      Not Heat-Treated<span class="sep">|</span>No Added Sugar
    </div>
    <div class="abs flavour">Orange Flavour</div>
  </section>
</body>
</html>
```